Web design for Money Service Business (uncoded)

We need a very basic website with 5-6 pages. Home page, Services, Transfer(How to use our service), About us, Contact us, FAQ
Our company name is Meridale Exchange. We are a company that deals with currency exchange and international money transfer. We do cash exchange and international money transfers to bank accounts all over the world. We offer highly competitive exchange rates so usually attract customers who transfer money over $10,000. Our niche is with larger sums of money, the design needs to be professional and communicate trust, security and stability.

```html
<!DOCTYPE html>
<html lang="en">
<head>
<meta charset="utf-8">
<title>About Us – Meridale Exchange</title>
<link href="https://fonts.googleapis.com/css2?family=Arimo:ital,wght@0,400;0,700;1,400&family=Delius&display=swap" rel="stylesheet">
<style>
:root{
  --brand-blue:#1f4e79;
  --accent:#f0a030;
  --text:#444;
  --muted:#888;
  --band:#f1f1f1;
  --footer:#f3f3f3;
  --card:#f7f7f7;
  --social:#8a2a5a;
  --rule:#dcdcdc;
  --white:#fff;
}
*{box-sizing:border-box;margin:0;padding:0}
html,body{width:1113px;height:1200px;overflow:hidden}
body{position:relative;background:var(--white);font-family:"Arimo",Arial,sans-serif;color:var(--muted)}
a{color:var(--accent);text-decoration:none}
b{color:#666}

.site-header{position:absolute;left:0;top:0;width:1113px;height:100px;background:var(--white);box-shadow:0 1px 3px rgba(0,0,0,.06)}
.brand{position:absolute;left:73px;top:31px}
.brand-name{font-size:23px;font-weight:700;color:var(--brand-blue);letter-spacing:.3px;line-height:1}
.brand-tag{font-size:8.6px;color:#5b88b3;letter-spacing:1.6px;margin-top:3px}
.main-nav{position:absolute;top:0;left:0}
.nav-item{position:absolute;top:0;height:80px;width:90px;margin-left:-45px;text-align:center;font-size:12px;color:var(--text)}
.nav-item svg{position:absolute;top:33px;left:40px}
.nav-item span{position:absolute;top:57px;left:0;width:100%}
.nav-item.active{background:#f4f4f4;border-top:3px solid var(--accent);width:71px;margin-left:-35.5px}
.nav-item.active svg{left:30px;top:30px}
.nav-item.active span{top:54px}

.page-band{position:absolute;left:0;top:100px;width:1113px;height:87px;background:var(--band)}
.page-icon{position:absolute;left:90px;top:27px}
.page-title{position:absolute;left:131px;top:30px;font-family:"Delius",cursive;font-size:23px;font-weight:400;color:var(--text)}
.page-sub{position:absolute;left:228px;top:36px;font-size:12px;font-style:italic;color:var(--muted)}
.page-sub::before{content:"/";font-size:22px;font-style:normal;color:var(--text);margin-right:8px;position:relative;top:3px}

.about-content{position:absolute;left:90px;top:232px;width:926px}
.about-content h2{font-size:14px;font-weight:700;color:var(--text);margin-bottom:8px}
.about-content p{font-size:10.6px;line-height:23.3px;margin-bottom:24px}

.team-heading{position:absolute;left:73px;top:602px;width:965px;height:24px;text-align:center}
.team-heading::before{content:"";position:absolute;left:0;right:0;top:13px;border-top:1px dashed var(--rule)}
.team-heading h2{position:relative;display:inline-block;background:var(--white);padding:0 14px;font-family:"Delius",cursive;font-size:21px;font-weight:400;color:var(--text)}

.team-card{position:absolute;top:665px;width:222px;height:237px;background:var(--card);border-bottom:2px solid var(--accent);text-align:center}
.team-photo{height:106px}
.team-card h3{font-size:11.5px;font-weight:700;color:var(--text);margin-top:20px}
.team-card p{font-size:10px;font-style:italic;line-height:19.5px;margin:9px 18px 0}
.team-links{margin-top:8px;display:flex;justify-content:center;gap:8px;align-items:center}
.team-links i{width:19px;height:19px;border-radius:50%;background:var(--social);display:block}
.team-links em{font-style:normal;font-size:21px;font-weight:700;color:var(--social);line-height:19px}

.site-footer{position:absolute;left:0;top:937px;width:1113px;height:263px;background:var(--footer)}
.footer-col{position:absolute;top:35px;width:205px}
.footer-col h4{font-size:11px;font-weight:700;color:var(--text);margin-bottom:10px}
.footer-col p{font-size:10px;line-height:20px}
.footer-col .more{display:block;font-size:10px;margin-top:8px}
.contact-list{list-style:none;font-size:10px;line-height:18px}
.contact-list li{position:relative;padding-left:15px;margin-bottom:11px}
.contact-list svg{position:absolute;left:0;top:4px}
.footer-rule{position:absolute;left:73px;top:216px;width:965px;border-top:1px dashed var(--rule)}
.copyright{position:absolute;left:73px;top:232px;font-size:10px}
.footer-social{position:absolute;right:75px;top:229px;display:flex;gap:11px}
.footer-social i{width:19px;height:19px;border-radius:50%;background:#8a8a8a;display:block}
</style>
</head>
<body>

<header class="site-header">
  <div class="brand">
    <div class="brand-name">MERIDALE EXCHANGE</div>
    <div class="brand-tag">INTERNATIONAL MONEY TRANSFER</div>
  </div>
  <nav class="main-nav">
    <a class="nav-item" style="left:591px"><svg width="10" height="10" viewBox="0 0 10 10"><path d="M5 0L0 5h1.5v5h2.5V7h2v3h2.5V5H10z" fill="#aaa"/></svg><span>HOME</span></a>
    <a class="nav-item" style="left:671px"><svg width="11" height="9" viewBox="0 0 11 9"><rect x="0" y="2" width="11" height="7" rx="1" fill="#aaa"/><rect x="3" y="0" width="5" height="3" fill="#aaa"/><circle cx="5.5" cy="5.5" r="2" fill="#fff"/></svg><span>TRANSFER</span></a>
    <a class="nav-item" style="left:763px"><svg width="11" height="9" viewBox="0 0 11 9"><rect y="0" width="11" height="2" fill="#aaa"/><rect y="3.5" width="11" height="2" fill="#aaa"/><rect y="7" width="11" height="2" fill="#aaa"/></svg><span>SERVICES</span></a>
    <a class="nav-item active" style="left:843px"><svg width="10" height="10" viewBox="0 0 10 10"><circle cx="5" cy="3" r="2.6" fill="#aaa"/><path d="M0 10c0-3 2-4.5 5-4.5S10 7 10 10z" fill="#aaa"/></svg><span>ABOUT</span></a>
    <a class="nav-item" style="left:922px"><svg width="11" height="8" viewBox="0 0 11 8"><rect width="11" height="8" rx="1" fill="#aaa"/><path d="M0 1l5.5 4L11 1" stroke="#fff" fill="none"/></svg><span>CONTACT</span></a>
    <a class="nav-item" style="left:994px"><svg width="12" height="9" viewBox="0 0 12 9"><ellipse cx="5" cy="3.5" rx="5" ry="3.5" fill="#aaa"/><ellipse cx="8" cy="5.5" rx="4" ry="3" fill="#aaa"/></svg><span>FAQ</span></a>
  </nav>
</header>

<section class="page-band">
  <svg class="page-icon" width="29" height="29" viewBox="0 0 29 29"><circle cx="14.5" cy="8" r="7.5" fill="#c4c4c4"/><path d="M0 29c0-9 6-13 14.5-13S29 20 29 29z" fill="#c4c4c4"/></svg>
  <h1 class="page-title">About Us</h1>
  <div class="page-sub">Below you can find more information about our company</div>
</section>

<main class="about-content">
  <h2>ABOUT MERIDALE EXCHANGE</h2>
  <p>Lorem ipsum dolor sit amet, consectetur adipisicing elit, sed do eiusmod tempor incididunt ut labore et. Ut wisi enim ad minim veniam, quis nostrud exerci tation ullamcorper <a>suscipit lobortis</a> nisl ut aliquip ex ea commodo consequat. Lorem ipsum <b>dolor sit amet</b>, consectetur adipisicing elit, sed do eiusmod tempor incididunt ut labore et. Ut wisi enim ad minim veniam, quis nostrud exerci tation ullamcorper suscipit lobortis nisl ut aliquip ex ea commodo consequat. Lorem ipsum dolor sit amet, consectetur adipisicing elit, sed do <b>eiusmod tempor</b> incididunt.</p>
  <h2>OUR MISSION</h2>
  <p>Lorem ipsum dolor sit amet, <a>consectetur adipisicing</a> elit, sed do eiusmod tempor incididunt ut labore et. Ut wisi enim ad minim veniam, quis nostrud exerci tation ullamcorper suscipit lobortis nisl ut aliquip ex ea commodo consequat. Lorem ipsum dolor sit amet, <b>consectetur adipisicing</b> elit, sed do eiusmod <a>tempor incididunt</a> ut labore et. Ut wisi enim ad minim veniam, quis nostrud exerci tation ullamcorper suscipit lobortis nisl ut aliquip ex ea commodo consequat. Lorem ipsum dolor sit amet, consectetur adipisicing elit, sed do eiusmod tempor incididunt.</p>
  <h2>WHY CHOOSE US</h2>
  <p>Lorem ipsum dolor sit amet, <b>consectetur adipisicing elit</b>, sed do eiusmod tempor incididunt ut labore et. Ut wisi enim ad minim veniam, quis nostrud exerci tation ullamcorper suscipit lobortis nisl ut aliquip ex ea commodo consequat. Lorem ipsum dolor sit amet, consectetur adipisicing elit, sed do eiusmod tempor incididunt ut labore et. Ut wisi enim ad minim veniam, quis <a>nostrud exerci</a> tation ullamcorper suscipit lobortis nisl ut aliquip ex ea commodo consequat. Lorem ipsum dolor sit amet, consectetur adipisicing elit, sed do eiusmod tempor incididunt.</p>
</main>

<div class="team-heading"><h2>Meet Our Team</h2></div>

<article class="team-card" style="left:73px">
  <div class="team-photo" role="img" aria-label="Team member photo: John Doe in an office" style="background:linear-gradient(135deg,#8a7a6a,#c9b9a5 55%,#6e5e52)"></div>
  <h3>JOHN DOE</h3>
  <p>Lorem ipsum dolor sit amet, consectetur adipisicing elit, sed do eiusmod tempor...</p>
  <div class="team-links"><i></i><i></i><i></i><em>@</em></div>
</article>
<article class="team-card" style="left:321px">
  <div class="team-photo" role="img" aria-label="Team member photo: Jane Doe at her desk" style="background:linear-gradient(135deg,#4a4a48,#8d8a6a 50%,#3b3b3a)"></div>
  <h3>JANE DOE</h3>
  <p>Lorem ipsum dolor sit amet, consectetur adipisicing elit, sed do eiusmod tempor...</p>
  <div class="team-links"><i></i><i></i><i></i><em>@</em></div>
</article>
<article class="team-card" style="left:569px">
  <div class="team-photo" role="img" aria-label="Team member photo: Tim Brown, black and white portrait" style="background:linear-gradient(135deg,#5a5a5a,#b5b5b5 50%,#3e3e3e)"></div>
  <h3>TIM BROWN</h3>
  <p>Lorem ipsum dolor sit amet, consectetur adipisicing elit, sed do eiusmod...</p>
  <div class="team-links"><i></i><i></i><i></i><em>@</em></div>
</article>
<article class="team-card" style="left:816px">
  <div class="team-photo" role="img" aria-label="Team member photo: Sarah Red in costume" style="background:linear-gradient(135deg,#6b6158,#a9805f 50%,#d9d3c4)"></div>
  <h3>SARAH RED</h3>
  <p>Lorem ipsum dolor sit amet, consectetur adipisicing elit, sed do eiusmod...</p>
  <div class="team-links"><i></i><i></i><i></i><em>@</em></div>
</article>

<footer class="site-footer">
  <div class="footer-col" style="left:73px">
    <h4>ABOUT US</h4>
    <p>Lorem ipsum dolor sit amet, consectetur adipisicing elit, sed do eiusmod tempor incididunt ut labore et. Lorem ipsum dolor sit amet, consectetur adipisicing elit, sed do eiusmod tempor incididunt ut labore et.</p>
    <a class="more">Read more...</a>
  </div>
  <div class="footer-col" style="left:322px"><h4>LATEST POSTS</h4></div>
  <div class="footer-col" style="left:569px"><h4>PHOTO STREAM</h4></div>
  <div class="footer-col" style="left:817px;width:220px">
    <h4>CONTACT US</h4>
    <ul class="contact-list">
      <li><svg width="7" height="10" viewBox="0 0 7 10"><path d="M3.5 0A3.5 3.5 0 0 0 0 3.5C0 6 3.5 10 3.5 10S7 6 7 3.5A3.5 3.5 0 0 0 3.5 0z" fill="#888"/><circle cx="3.5" cy="3.5" r="1.3" fill="#f3f3f3"/></svg>Address: Corso Lavandine 14, 20121, Milano, MI, Italy</li>
      <li><svg width="9" height="9" viewBox="0 0 9 9"><path d="M1 0l2 2-1 1.5c.8 1.5 2 2.7 3.5 3.5L7 6l2 2-1.5 1C3.5 8.5.5 5.5 0 1.5z" fill="#888"/></svg>Phone: 0039 340 55 21 908</li>
      <li><svg width="9" height="9" viewBox="0 0 10 10"><circle cx="5" cy="3" r="2.6" fill="#888"/><path d="M0 10c0-3 2-4.5 5-4.5S10 7 10 10z" fill="#888"/></svg>Chat: Meridale_Exchange</li>
      <li><svg width="10" height="8" viewBox="0 0 11 8"><rect width="11" height="8" rx="1" fill="#888"/><path d="M0 1l5.5 4L11 1" stroke="#f3f3f3" fill="none"/></svg>Email: <a>info@meridale-exchange.com</a></li>
    </ul>
  </div>
  <div class="footer-rule"></div>
  <div class="copyright">Copyright 2012 Meridale Exchange - All rights reserved.</div>
  <div class="footer-social"><i></i><i></i><i></i><i></i></div>
</footer>

</body>
</html>
```